Grins of Maplecrest - Dental, needs a redesign

Purpose:
Redesign website: http://www.grinsofmaplecrest.example/

Sections are important, but for content, we can use existing website or have some placeholder text to fill in later.

Some of the required sections:
About us, contact us, services, our offices, our staff, patient education, patient forms (link to Molvaro can be used here), link to friendwall, testimonials

Editability:
We would like to be able to update and edit the content in the future, for small changes

Pictures:
Here is a link to the staff pictures we’d like to use on the website:
https://www.filecrate.example/sh/503k7pq2vv884x9/BBDPyrTe_wKQj7ZumfXKTgghb?dl=0
You don't have to use all the pictures; just a few.

Friendwall page:
https://www.friendwall.example/Grins-of-Maplecrest-527163048915276

Colors: Calming colors/images for a soothing feeling... to assure the patient that it'll not be that bad.

Target Market(s)

General population

Industry/Entity Type

Dental Clinic

Coding

Coded - Design and coding required

Number of Pages Required

5+ page

Requirements
Must have
• About us, contact us, services, our offices, our staff, patient education, patient forms (link to Molvaro can be used here), link to friendwall, testimonials.
• Just create the placeholders for content or use from existing website.
• The staff picture of everyone needs to be on the home page - because that makes it more personal and has received positive feedback from many patients.

```html
<!DOCTYPE html>
<html lang="en">
<head>
<meta charset="utf-8">
<title>Grins of Maplecrest – Services</title>
<link href="https://fonts.googleapis.com/css2?family=Open+Sans:wght@400;600&family=Roboto:wght@300;400;500;700&display=swap" rel="stylesheet">
<style>
:root{
  --purple:#7a55bd;
  --purple-line:#6b3fb8;
  --teal:#24aab7;
  --ink:#444;
  --muted:#777;
  --page:#f4f4f4;
  --card-border:#e2e2e2;
  --footer:#262626;
  --footer-bar:#1c1c1c;
  --footer-text:#bdbdbd;
  --white:#fff;
}
*{box-sizing:border-box;margin:0;padding:0}
html,body{width:732px;height:1200px;overflow:hidden}
body{font-family:"Open Sans",sans-serif;color:var(--ink);background:var(--white);position:relative}
.site-header{position:absolute;top:0;left:0;width:732px;height:72px;border-top:2px solid var(--purple-line);background:var(--white)}
.brand{position:absolute;left:60px;top:14px;display:flex;align-items:center;gap:10px}
.brand-dot{width:34px;height:34px;border-radius:50%;background:var(--teal)}
.brand-name{font-family:"Roboto",sans-serif;font-weight:300;color:var(--teal);font-size:15px;line-height:19px;letter-spacing:.5px;width:100px}
.main-nav{position:absolute;right:60px;top:30px;display:flex;gap:13px;font-size:7.4px;color:#555}
.main-nav .active{color:var(--purple)}
.hero{position:absolute;top:72px;left:0;width:732px;height:290px}
.hero svg{position:absolute;top:0;left:0}
.hero-copy{position:absolute;left:373px;top:70px;color:var(--white)}
.hero-kicker{font-family:"Roboto",sans-serif;font-weight:700;font-size:19px;letter-spacing:-.3px}
.hero-title{font-family:"Roboto",sans-serif;font-weight:300;font-size:36px;color:var(--purple);line-height:44px;letter-spacing:-.5px}
.hero-lead{font-size:11.2px;line-height:20px;margin-top:8px;width:270px}
.hero-btn{display:inline-block;margin-top:11px;background:var(--purple);color:var(--white);font-size:8.6px;padding:9px 16px;border-radius:2px}
.slider-arrows{position:absolute;left:76px;top:201px;display:flex;gap:2px}
.slider-arrows span{width:14px;height:14px;background:#777;color:#fff;font-size:9px;line-height:14px;text-align:center}
.services-intro{position:absolute;top:362px;left:0;width:732px;height:90px;background:var(--teal);color:var(--white);text-align:center}
.services-intro h1{font-family:"Roboto",sans-serif;font-weight:400;font-size:15px;margin-top:10px}
.services-intro p{font-size:6.6px;line-height:15.5px;width:560px;margin:8px auto 0}
.services-list{position:absolute;top:452px;left:0;width:732px;height:531px;background:var(--page)}
.service-card{position:absolute;left:60px;width:612px;height:139px;background:var(--white);border:1px solid var(--card-border)}
.service-photo{position:absolute;left:35px;top:18px;width:97px;height:97px;border-radius:50%;border-bottom:3px solid var(--teal);border-left:2px solid var(--purple)}
.service-body{position:absolute;left:166px;top:18px;width:430px}
.service-body h2{font-family:"Open Sans",sans-serif;font-weight:400;font-size:8.4px;color:var(--purple);margin-bottom:10px}
.service-body p{font-size:6.3px;line-height:13.5px;color:var(--muted);margin-bottom:8px}
.service-body a{font-size:6.4px;color:var(--purple);text-decoration:none}
.site-footer{position:absolute;top:983px;left:0;width:732px;height:167px;background:var(--footer);color:var(--footer-text)}
.footer-col{position:absolute;top:24px}
.footer-col h3{font-family:"Roboto",sans-serif;font-weight:400;font-size:9.6px;color:var(--white);margin-bottom:10px}
.hours li{list-style:none;font-size:6.3px;line-height:15.6px}
.contact-item{display:flex;gap:8px;font-size:6.3px;line-height:15.6px;margin-bottom:7px}
.contact-item svg{flex:none;margin-top:3px}
.map{position:absolute;left:458px;top:26px;width:213px;height:109px;background:linear-gradient(135deg,#ece8dc,#d9dfd0 55%,#c9d6e3)}
.footer-bar{position:absolute;top:1150px;left:0;width:732px;height:50px;background:var(--footer-bar);color:#ddd;font-size:6.3px}
.footer-links{position:absolute;left:59px;top:14px}
.copyright{position:absolute;left:59px;top:30px}
.follow{position:absolute;left:558px;top:14px;display:flex;align-items:center;gap:4px}
.follow span{margin-right:3px}
.follow i{width:18px;height:18px;border-radius:50%;background:var(--white);display:block}
</style>
</head>
<body>
<header class="site-header">
  <div class="brand"><span class="brand-dot"></span><span class="brand-name">Grins of Maplecrest</span></div>
  <nav class="main-nav">
    <span>Home</span><span>About us</span><span class="active">Services</span><span>Our offices</span><span>Our staff</span><span>Patient education</span><span>Patient forms</span><span>Testimonials</span><span>Contact us</span>
  </nav>
</header>

<section class="hero">
  <svg width="732" height="290" viewBox="0 0 732 290">
    <defs>
      <linearGradient id="staff" x1="0" y1="0" x2="1" y2="1">
        <stop offset="0" stop-color="#8a7a66"/><stop offset=".5" stop-color="#4a3f38"/><stop offset="1" stop-color="#2b2a2c"/>
      </linearGradient>
    </defs>
    <rect width="732" height="290" fill="url(#staff)" role="img" aria-label="Group photo of the clinic staff seated together"/>
    <path d="M0 188 C120 290 300 300 460 288 L460 290 L0 290Z" fill="#7a55bd"/>
    <path d="M0 228 C200 312 480 292 732 184 L732 290 L0 290Z" fill="#24aab7"/>
  </svg>
  <div class="slider-arrows"><span>‹</span><span>›</span></div>
  <div class="hero-copy">
    <div class="hero-kicker">GRINS OF MAPLECREST</div>
    <div class="hero-title">HONESTLY CARING</div>
    <p class="hero-lead">Welcome to grinsofmaplecrest dental surgery &amp; Quality Dentistry...</p>
    <span class="hero-btn">Click here for more info</span>
  </div>
</section>

<section class="services-intro">
  <h1>Services</h1>
  <p>We change lives daily by creating healthy, beautiful smiles that allow patients to confidently put their best face forward.We know time is important to you. Our team works efficiently to address your concerns, get you in, out, and on with your day, while providing you with excellent oral health care...</p>
</section>

<main class="services-list">
  <article class="service-card" style="top:26px">
    <div class="service-photo" role="img" aria-label="Dental model with toothbrush" style="background:radial-gradient(circle,#eee,#9a9a9a)"></div>
    <div class="service-body">
      <h2>Fillings</h2>
      <p>Fillings are done to remove decay, and replace the affected tooth structure. It is called a filling because new a material fills hole that decay left. Now days most teeth are treated with bonded tooth colored composite resin</p>
      <p>FillingsCaught early enough, cavities can be treated easily and painlessly. If not treated decay can lead to tooth pain and/or infection, and the tooth would need root canal treatment or extraction.</p>
      <a href="#">Click read More Information</a>
    </div>
  </article>
  <article class="service-card" style="top:188px">
    <div class="service-photo" role="img" aria-label="X-ray viewing monitor" style="background:radial-gradient(circle,#555,#cfd3d6)"></div>
    <div class="service-body">
      <h2>X-Rays</h2>
      <p>This is a focused beam of X-Ray particles through bone which produces an image on special film, showing the structure through which it passed. This gives the familiar black and white images that doctors and dentists use to diagnose problems.</p>
      <p>X-rays are a necessary part of the diagnostic process, and not to use them could lead to undiagnosed disease. Without an X-ray of the whole tooth, and supporting bone and gum tissues, there is no real way to detect infection or pathology that requires attention.</p>
      <a href="#">Click read More Information</a>
    </div>
  </article>
  <article class="service-card" style="top:351px">
    <div class="service-photo" role="img" aria-label="Dentist talking with a patient" style="background:linear-gradient(135deg,#d8d2c6,#c98a66)"></div>
    <div class="service-body">
      <h2>Non-surgical Gum Treatments</h2>
      <p>The gums, ligaments, and bone around the teeth form the foundation for ones teeth. All structures are also referred to as the periodontium. When the periodontium is not healthy, it jeopardizes the teeth just as a bad foundation</p>
      <p>Would threaten the stability of a house. Signs of unhealthy periodontium (gum disease) may be as follows: gums that are red and bleed easily, persistent bad breath gums that are pulled away from the tooth...</p>
      <a href="#">Click read More Information</a>
    </div>
  </article>
</main>

<footer class="site-footer">
  <div class="footer-col" style="left:60px">
    <h3>Clinic Timinigs</h3>
    <ul class="hours">
      <li>Monday: 12:00pm to 6:00pm</li>
      <li>Tuesday: 10:00am to 7:00pm</li>
      <li>Wednesday: Closed</li>
      <li>Thursday: 8:00am to 6:00pm</li>
      <li>Friday: 8:00am to 5:00pm</li>
      <li>Saturday when open: 8:00am to 3:00pm OR 8:00am to 12:00pm</li>
    </ul>
  </div>
  <div class="footer-col" style="left:298px">
    <h3>Contact info</h3>
    <div class="contact-item"><svg width="7" height="10" viewBox="0 0 7 10"><path d="M3.5 0A3.5 3.5 0 0 0 0 3.5C0 6 3.5 10 3.5 10S7 6 7 3.5A3.5 3.5 0 0 0 3.5 0Zm0 5A1.5 1.5 0 1 1 3.5 2a1.5 1.5 0 0 1 0 3Z" fill="#bbb"/></svg><span>418 Alder Ridge Rd, Suite 2C<br>Maplecrest, IL 60999</span></div>
    <div class="contact-item"><svg width="9" height="9" viewBox="0 0 9 9"><path d="M2 0l1.6 2.2-1 1.2a6 6 0 0 0 3 3l1.2-1L9 7l-1 2C3.5 9 0 5.5 0 1Z" fill="#bbb"/></svg><span>Call us at: 555-014-2210/2211</span></div>
    <div class="contact-item"><svg width="10" height="8" viewBox="0 0 10 8"><rect width="10" height="8" rx="1" fill="#bbb"/><path d="M0 1l5 3.5L10 1" stroke="#262626" fill="none"/></svg><span>info@grinsofmaplecrest.example</span></div>
  </div>
  <div class="map" role="img" aria-label="Street map showing the clinic location"></div>
</footer>

<div class="footer-bar">
  <div class="footer-links">Home / About us / Services / our offices / our staff / Patient education / Patient forms / Testimonials / contact us.</div>
  <div class="copyright">Copyrights@grinsofmaplecrest.2016 | Allrights Reserved.</div>
  <div class="follow"><span>Follow With Us :</span><i></i><i></i><i></i></div>
</div>
</body>
</html>
```